Business Card Design - Carrington Hill Lodge

We are looking at a new design for our business cards that has a modern and professional look. We run a residential aged care facility focussing on the care of residents. The cards will be used for potential clients, consultants and business opportunities in this sector. Blue and white is our main colours and would to see these colours incorporated in the design.
Industry/Entity Type
Business
Contact Information for Business Card
Carrington Hill Lodge, Darren Pelham, dpelham@carringtonhilllodge.com.au, Finance Manager, 0491 736 208, BCom, 48 Yarrabee Way, Hollowbrook, Qld 4215.

```html
<!DOCTYPE html>
<html lang="en">
<head>
<meta charset="utf-8">
<title>Carrington Hill Lodge – Business Cards</title>
<link rel="stylesheet" href="https://fonts.googleapis.com/css2?family=Open+Sans:wght@300;400;700&display=swap">
<style>
  :root {
    --stage: #d4d4d4;
    --stage-light: #ececec;
    --card-white: #ffffff;
    --brand-blue: #6e8fa9;
    --brand-blue-dark: #587891;
    --brand-blue-deep: #4d6a82;
    --brand-taupe: #b9b2a8;
    --text-blue: #6a8aa3;
    --text-white: #f4f6f8;
  }
  * { box-sizing: border-box; margin: 0; padding: 0; }
  html, body { width: 1200px; height: 888px; overflow: hidden; }
  body {
    background: radial-gradient(ellipse at 50% 40%, var(--stage-light) 0%, var(--stage) 75%);
    font-family: "Open Sans", sans-serif;
    position: relative;
  }
  .card {
    position: absolute;
    left: 320px;
    width: 560px;
    height: 320px;
    overflow: hidden;
    box-shadow: 0 6px 18px rgba(0,0,0,0.18);
  }
  .card--front { top: 100px; background: var(--card-white); }
  .card--back {
    top: 468px;
    background: radial-gradient(ellipse at 40% 30%, var(--brand-blue) 0%, var(--brand-blue-dark) 60%, var(--brand-blue-deep) 100%);
  }
  .card svg.card__shapes { position: absolute; inset: 0; }

  .brand {
    position: absolute;
    left: 30px;
    top: 34px;
    display: flex;
    align-items: center;
    gap: 10px;
    color: var(--brand-blue);
    font-weight: 700;
    font-size: 17px;
  }
  .brand__dot {
    width: 14px; height: 14px;
    border-radius: 50%;
    background: var(--brand-blue);
  }

  .contact {
    position: absolute;
    left: 262px;
    top: 58px;
    color: var(--text-blue);
  }
  .contact__name { font-weight: 700; font-size: 22px; line-height: 1.1; }
  .contact__role { font-size: 11px; margin-bottom: 10px; }
  .contact__line { font-size: 16px; line-height: 1.3; }
  .contact__phone { margin-top: 2px; }
  .contact__email { font-size: 14.5px; margin-top: 6px; }

  .back__brand {
    position: absolute;
    right: 40px;
    bottom: 40px;
    text-align: right;
    color: var(--text-white);
  }
  .back__name {
    font-weight: 700;
    font-size: 22px;
    line-height: 1.2;
  }
  .back__tagline {
    font-weight: 300;
    font-size: 13px;
    letter-spacing: 0.4px;
    margin-top: 2px;
  }
</style>
</head>
<body>

  <section class="card card--front" aria-label="Business card front">
    <svg class="card__shapes" width="560" height="320" viewBox="0 0 560 320" aria-hidden="true">
      <path d="M0,210 Q330,222 560,320 L490,320 Q300,252 0,246 Z" fill="var(--brand-blue)"/>
      <path d="M0,246 Q300,252 490,320 L440,320 Q270,268 0,262 Z" fill="var(--brand-taupe)"/>
    </svg>

    <div class="brand">
      <span class="brand__dot"></span>
      <span class="brand__name">Carrington Hill Lodge</span>
    </div>

    <div class="contact">
      <p class="contact__name">Darren Pelham</p>
      <p class="contact__role">Finance Manager, BCom</p>
      <p class="contact__line">48 Yarrabee Way</p>
      <p class="contact__line">Hollowbrook, Qld 4215</p>
      <p class="contact__line contact__phone">0491 736 208</p>
      <p class="contact__line contact__email">dpelham@carringtonhilllodge.com.au</p>
    </div>
  </section>

  <section class="card card--back" aria-label="Business card back">
    <svg class="card__shapes" width="560" height="320" viewBox="0 0 560 320" aria-hidden="true">
      <path d="M60,62 Q250,20 300,150" fill="none" stroke="var(--text-white)" stroke-width="4" stroke-linecap="round" opacity="0.85"/>
    </svg>

    <div class="back__brand">
      <p class="back__name">Carrington Hill Lodge</p>
      <p class="back__tagline">Care, Respect, Community</p>
    </div>
  </section>

</body>
</html>
```